Business Card for Start Up Real Estate Company

We need a business card designed for a new real estate company called Belvanta. We plan on improving the experience of real estate transactions for both consumers and agents by using current and evolving technology. We would like to see designs that use our existing logo (attached). Please use a primarily white or light colored background. The final design should communicate technology, sophistication and customer service. Thank you...

Industry/Entity Type

Real Estate

Requirements
Must have
• Primarily white or light colored background
Nice to have
• Isolated A from our logo used as part of the design
Should not have
• Pictures, especially of houses

```html
<!DOCTYPE html>
<html lang="en">
<head>
<meta charset="utf-8">
<title>Belvanta Business Card</title>
<link rel="stylesheet" href="https://fonts.googleapis.com/css2?family=Montserrat:wght@400;500;600&family=Oswald:wght@500&display=swap">
<style>
  :root {
    --backdrop: #8f9194;
    --card-white: #f7f9fb;
    --haze-light: #eef3f7;
    --haze-mid: #d9e3ec;
    --brand-blue: #1f5f9e;
    --brand-red: #e5223d;
    --text-blue: #1f5f9e;
  }
  * { box-sizing: border-box; margin: 0; padding: 0; }
  html, body {
    width: 1200px;
    height: 900px;
    overflow: hidden;
  }
  body {
    background: var(--backdrop);
    font-family: "Montserrat", Arial, sans-serif;
    position: relative;
  }
  .card {
    position: absolute;
    left: 330px;
    width: 540px;
    height: 310px;
    border-radius: 26px;
    overflow: hidden;
    background: var(--card-white);
    box-shadow: 0 10px 24px rgba(0, 0, 0, 0.25);
  }
  .card--front { top: 95px; }
  .card--back { top: 495px; }

  .card__backdrop {
    position: absolute;
    inset: 0;
    background: linear-gradient(120deg, var(--card-white) 0%, var(--haze-light) 45%, var(--haze-mid) 100%);
  }

  .brand-name {
    position: absolute;
    left: 150px;
    top: 130px;
    font-weight: 600;
    font-size: 50px;
    letter-spacing: 2px;
    color: var(--brand-blue);
  }

  .brand-feature {
    position: absolute;
    right: 0;
    top: 0;
    width: 250px;
    height: 310px;
    background: linear-gradient(160deg, rgba(31, 95, 158, 0.55) 0%, rgba(31, 95, 158, 0.25) 50%, rgba(229, 34, 61, 0.35) 100%);
    clip-path: polygon(40% 0, 100% 0, 100% 100%, 0 100%);
  }

  .name-tag {
    position: absolute;
    left: 30px;
    top: 48px;
    height: 34px;
    padding: 0 18px 0 46px;
    border-radius: 6px;
    background: var(--brand-blue);
    display: flex;
    align-items: center;
  }
  .name-tag__icon {
    position: absolute;
    left: 4px;
    top: 2px;
  }
  .name-tag__name {
    font-family: "Oswald", "Arial Narrow", sans-serif;
    font-weight: 500;
    font-size: 21px;
    letter-spacing: 2px;
    color: #fff;
  }

  .contact-list {
    position: absolute;
    left: 38px;
    top: 108px;
    list-style: none;
  }
  .contact-list__item {
    display: flex;
    align-items: center;
    gap: 14px;
    margin-bottom: 16px;
  }
  .contact-list__icon { flex: none; }
  .contact-list__text {
    font-size: 13px;
    line-height: 1.3;
    color: var(--text-blue);
  }
</style>
</head>
<body>

  <section class="card card--front" aria-label="Business card front">
    <div class="card__backdrop" role="img" aria-label="Soft pale blue architectural glass backdrop"></div>
    <div class="brand-name">BELVANTA</div>
  </section>

  <section class="card card--back" aria-label="Business card back">
    <div class="card__backdrop" role="img" aria-label="Soft pale blue architectural glass backdrop"></div>
    <div class="brand-feature" role="img" aria-label="Large brand letter decoration area"></div>

    <div class="name-tag">
      <svg class="name-tag__icon" width="30" height="30" viewBox="0 0 30 30" aria-hidden="true">
        <circle cx="15" cy="15" r="14" fill="var(--brand-red)"/>
        <circle cx="15" cy="11.5" r="4.5" fill="#fff"/>
        <path d="M7 23c1.5-4.5 4.5-6 8-6s6.5 1.5 8 6z" fill="#fff"/>
      </svg>
      <span class="name-tag__name">DANA HOLT</span>
    </div>

    <ul class="contact-list">
      <li class="contact-list__item">
        <svg class="contact-list__icon" width="22" height="22" viewBox="0 0 22 22" aria-hidden="true">
          <circle cx="11" cy="11" r="11" fill="var(--brand-red)"/>
          <path d="M11 5a4 4 0 0 0-4 4c0 3 4 8 4 8s4-5 4-8a4 4 0 0 0-4-4z" fill="#fff"/>
          <circle cx="11" cy="9" r="1.5" fill="var(--brand-red)"/>
        </svg>
        <span class="contact-list__text">Suite 4, 18 Marlow Crescent<br>Kellerton WA 6170</span>
      </li>
      <li class="contact-list__item">
        <svg class="contact-list__icon" width="22" height="22" viewBox="0 0 22 22" aria-hidden="true">
          <circle cx="11" cy="11" r="11" fill="var(--brand-red)"/>
          <path d="M7.5 5.5l2 .3 1 3-1.3 1a7 7 0 0 0 3 3l1-1.3 3 1 .3 2c-.5 1-1.5 1.3-2.5 1.2A9 9 0 0 1 6.3 8c-.1-1 .2-2 1.2-2.5z" fill="#fff"/>
        </svg>
        <span class="contact-list__text">P: (08) 5550 2741<br>F: (08) 5550 2742</span>
      </li>
      <li class="contact-list__item">
        <svg class="contact-list__icon" width="22" height="22" viewBox="0 0 22 22" aria-hidden="true">
          <circle cx="11" cy="11" r="11" fill="var(--brand-red)"/>
          <rect x="5.5" y="7" width="11" height="8" rx="1" fill="#fff"/>
          <path d="M5.5 7.5l5.5 4 5.5-4" fill="none" stroke="var(--brand-red)" stroke-width="1.2"/>
        </svg>
        <span class="contact-list__text">dholt@belvanta.com.au<br>www.belvanta.com.au</span>
      </li>
    </ul>
  </section>

</body>
</html>
```